Website for Public Relations Agency called "Tall Pine"

A need a website for a new business which is essentially a Public Relations/ Marketing business. We offer services to small family businesses, medium enterprise as well as multinational companies (ie we sell our professional services to other businesses; we are not a consumer brand).
The website needs to be polished, professional and modern. Because of the services we offer, I really need the website to be a little bit "wow".
Colours - we have a logo (see files) so the colour palette for the website should be dictated by this.
The Word doc attached mapped out the various pages that will make up the site. The text is not 100% finalised but it's good enough to give you a good picture of what the site will talk about.
I am not selling directly off my site, so this is an informational site only to explain who i am and what i do.
Target Market(s)
Other businesses - small family business, medium business and large multinational companies
Industry/Entity Type
Marketing
Coding
Coded - Design and coding required
Number of Pages Required
5+ page
Requirements
Must have
- Given my business, really looking for a little "wow" factor on the home page
Should not have
- I don't know if this is relevant to the coding, but I want to end up on a platform that I can myself make copy/ text edits as I please. I do not want to have to go through a deisgn company for small text changes in 6 or 12 months time.

```html
<!DOCTYPE html>
<html lang="en">
<head>
<meta charset="utf-8">
<title>Tall Pine – Strategic Communication</title>
<link href="https://fonts.googleapis.com/css2?family=Lato:wght@400;700;900&family=Poppins:wght@400;500;600;700&display=swap" rel="stylesheet">
<style>
:root{
  --pink:#d94fa0;
  --purple:#9b7fb8;
  --card:#957db4;
  --navy:#2b2a63;
  --ink:#2a2a2a;
  --grey:#555;
  --footer:#141414;
  --footer-base:#1b1b1b;
  --white:#fff;
}
*{margin:0;padding:0;box-sizing:border-box}
html,body{width:1200px;height:2852px;overflow:hidden}
body{position:relative;font-family:'Lato',sans-serif;color:var(--ink);background:var(--white)}
.abs{position:absolute}
a{color:inherit;text-decoration:none}

/* hero */
.hero{left:0;top:0;width:1200px;height:643px;background:linear-gradient(120deg,#2a2326 0%,#1e1a1d 50%,#2c2429 100%)}
.hero-portrait{left:660px;top:160px;width:430px;height:483px;background:linear-gradient(180deg,#6a5650 0%,#3f87d6 55%,#2f7bd1 100%);border-radius:200px 200px 0 0}
.brand{font-family:'Lato',sans-serif;font-weight:700;color:var(--pink);display:flex;align-items:center;gap:10px}
.brand-mark{width:26px;height:26px;background:var(--purple)}
.brand-top{left:111px;top:34px;font-size:38px}
.nav{top:46px;font-size:16px;font-weight:700;color:var(--white)}
.nav.active{text-decoration:underline}
.btn{background:var(--pink);color:var(--white);font-weight:700;display:flex;align-items:center;justify-content:center;border-radius:0 12px 0 12px}
.btn-contact{left:926px;top:33px;width:162px;height:47px;font-size:16px}
.hero h1{left:111px;top:222px;font-size:45px;line-height:50px;font-weight:400;color:var(--white)}
.hero-sub{left:111px;top:333px;font-size:20.5px;line-height:29px;color:var(--white)}
.hero-text{left:111px;top:400px;width:520px;font-size:13px;line-height:22px;color:var(--white)}
.btn-start{left:111px;top:464px;width:146px;height:47px;font-size:16px}

/* messaging */
.messaging-visual{left:111px;top:740px;width:416px;height:543px;background:linear-gradient(135deg,#f2a6d2 0%,#d94fa0 40%,#b497cf 70%,#8b6cb0 100%);opacity:.75}
.msg-title{left:596px;top:775px;font-size:40px;line-height:46px;font-weight:700}
.pink{color:var(--pink)} .purple{color:var(--purple)}
.rule{height:3px;background:var(--pink)}
.msg-list{left:596px;top:918px;width:500px;list-style:none}
.msg-list li{position:relative;padding-left:41px;font-size:15.5px;line-height:25px;margin-bottom:10px;color:#333}
.msg-list li::before{content:"?";position:absolute;left:0;top:5px;width:14px;height:14px;border-radius:50%;background:var(--pink);color:var(--white);font-size:10px;font-weight:900;line-height:14px;text-align:center}

/* get in touch */
.touch{left:0;top:1379px;width:1200px;height:445px;background:radial-gradient(ellipse at 20% 90%,#3b3a8a 0%,var(--navy) 55%),var(--navy)}
.touch-title{left:0;top:1462px;width:1200px;text-align:center;font-family:'Poppins',sans-serif;font-weight:600;font-size:38px;color:var(--white)}
.touch-text{left:150px;top:1545px;width:900px;text-align:center;font-family:'Poppins',sans-serif;font-size:25px;line-height:36px;color:var(--white)}
.btn-today{left:497px;top:1686px;width:206px;height:47px;font-family:'Poppins',sans-serif;font-size:14.5px;font-weight:600}

/* services */
.help-title{left:0;top:1915px;width:1200px;text-align:center;font-size:44px;line-height:48px;font-weight:700}
.slide{top:2130px;width:300px;text-align:center;font-size:26px;line-height:31px;color:var(--grey)}
.slide-card{left:458px;top:2071px;width:320px;height:196px;background:var(--card);border-radius:0 0 14px 0;display:flex;align-items:center;justify-content:center;text-align:center;padding:0 16px;font-family:'Poppins',sans-serif;font-size:22px;line-height:31px;font-weight:600;color:var(--white)}
.arrow{width:28px;height:28px;border-radius:50%;background:var(--pink)}

/* footer */
.footer{left:0;top:2370px;width:1200px;height:322px;background:var(--footer)}
.brand-foot{left:70px;top:2470px;font-size:36px}
.divider{top:2405px;width:1px;height:265px;background:#333}
.foot-head{top:2425px;font-size:22px;font-weight:700;color:var(--pink)}
.foot-links{left:400px;top:2475px;list-style:none;color:var(--white);font-size:15px}
.foot-links li{height:38.5px}
.foot-item{display:flex;align-items:center;gap:20px;color:var(--white);font-family:'Poppins',sans-serif;font-size:15px}
.foot-icon{width:34px;height:34px;border-radius:50%;background:#2a2a2a;display:flex;align-items:center;justify-content:center}
.base{left:0;top:2692px;width:1200px;height:160px;background:var(--footer-base)}
.ack{left:111px;top:2724px;width:980px;font-size:12.5px;line-height:22px;color:#8a8a8a}
.copy{left:111px;top:2808px;font-size:13px;color:var(--white)}
</style>
</head>
<body>

<section class="abs hero" role="img" aria-label="Dark blurred photo of a desk covered with printed media and notes"></section>
<div class="abs hero-portrait" role="img" aria-label="Portrait of the founder in a bright blue blazer"></div>

<div class="abs brand brand-top"><span class="brand-mark"></span>Tall Pine</div>
<a class="abs nav active" style="left:510px">Home</a>
<a class="abs nav" style="left:592px">About Us</a>
<a class="abs nav" style="left:697px">How We Help</a>
<a class="abs nav" style="left:836px">Fees</a>
<a class="abs btn btn-contact">CONTACT NOW</a>

<div class="hero">
  <h1 class="abs">Carefully considered.<br>Expertly crafted.</h1>
  <p class="abs hero-sub">Strategic Communication &amp; Reputation<br>Management Specialist</p>
  <p class="abs hero-text">When you have a message to deliver, a story to tell, something to say that you need your stakeholders to hear loud and clear… Tall Pine can help.</p>
  <a class="abs btn btn-start">GET STARTED</a>
</div>

<div class="abs messaging-visual" role="img" aria-label="Tinted collage of people in meetings and at work"></div>
<h2 class="abs msg-title"><span class="pink">In business, messaging</span><br><span class="purple">always matters</span></h2>
<div class="abs rule" style="left:596px;top:881px;width:75px"></div>
<ul class="abs msg-list">
  <li>Do you have a message to share that will build trust with the audiences that drive your revenue?</li>
  <li>Perhaps you need help promoting your people or services, or ensure they are known by a wider audience?</li>
  <li>Is there a narrative to be carefully devised and managed to prevent the erosion of trust amongst your important stakeholders, either internal or external?</li>
  <li>Do you have a situation on your hands, and you feel like you need to go into damage control?</li>
  <li>Has the media come knocking and you’re not sure what to say?</li>
  <li>Do you need a website that is cohesive and sharp?</li>
</ul>

<section class="abs touch"></section>
<h2 class="abs touch-title">Get in touch</h2>
<div class="abs rule" style="left:563px;top:1518px;width:75px"></div>
<p class="abs touch-text">We’d love to talk about how we can help shape your narrative, overcome your communications challenges, and support you to say what needs to be said.</p>
<a class="abs btn btn-today">CONTACT US TODAY!</a>

<h2 class="abs help-title"><span class="pink">We Help You Communicate With</span><br><span class="purple">Clarity &amp; Impact</span></h2>
<div class="abs rule" style="left:563px;top:2021px;width:75px"></div>
<div class="abs arrow" style="left:41px;top:2156px"><svg width="28" height="28" viewBox="0 0 28 28"><path d="M16 9l-5 5 5 5" stroke="#fff" stroke-width="2.5" fill="none" stroke-linecap="round"/></svg></div>
<p class="abs slide" style="left:90px">Media strategy, liaison, management and execution</p>
<div class="abs slide-card">Crisis, Issues &amp; Reputation Management (specialising in post cyber incident communications)</div>
<p class="abs slide" style="left:825px">Executive &amp; Internal Communication</p>
<div class="abs arrow" style="left:1130px;top:2156px"><svg width="28" height="28" viewBox="0 0 28 28"><path d="M12 9l5 5-5 5" stroke="#fff" stroke-width="2.5" fill="none" stroke-linecap="round"/></svg></div>

<footer class="abs footer"></footer>
<div class="abs brand brand-foot"><span class="brand-mark"></span>Tall Pine</div>
<div class="abs divider" style="left:346px"></div>
<div class="abs divider" style="left:585px"></div>
<div class="abs divider" style="left:954px"></div>

<h3 class="abs foot-head" style="left:398px">QUICK LINKS</h3>
<ul class="abs foot-links">
  <li>Home</li><li>About</li><li>How We Help</li><li>Fees</li><li>Get in Touch</li>
</ul>

<h3 class="abs foot-head" style="left:630px">CONTACT US</h3>
<div class="abs foot-item" style="left:631px;top:2485px"><span class="foot-icon"><svg width="14" height="14" viewBox="0 0 14 14"><path d="M7 1a4 4 0 0 0-4 4c0 3 4 8 4 8s4-5 4-8a4 4 0 0 0-4-4z" fill="#fff"/><circle cx="7" cy="5" r="1.5" fill="#2a2a2a"/></svg></span>Address city, state, zip</div>
<div class="abs foot-item" style="left:631px;top:2540px"><span class="foot-icon"><svg width="14" height="14" viewBox="0 0 14 14"><path d="M3 1l2 3-1.5 1.5c.8 1.8 2.2 3.2 4 4L9 8l3 2-1 2.5C6 12 2 8 1.5 3z" fill="#fff"/></svg></span>000.111.222.333</div>
<div class="abs foot-item" style="left:631px;top:2594px"><span class="foot-icon"><svg width="14" height="14" viewBox="0 0 14 14"><rect x="1" y="3" width="12" height="8" fill="#fff"/><path d="M1 3l6 5 6-5" stroke="#2a2a2a" fill="none"/></svg></span>email@tallpine.example</div>

<h3 class="abs foot-head" style="left:999px">FOLLOW US</h3>
<div class="abs foot-item" style="left:999px;top:2485px"><span class="foot-icon"></span>ProfileHub</div>

<div class="abs base"></div>
<p class="abs ack">Tall Pine acknowledges the Traditional Owners of Country throughout the land we call Australia. In particular, we pay our respect to the Cameraygal people of the Eora nation whose Country our business operates from. Indeed, we recognise all First Nations peoples’ continuing connection to land, waters and culture and pay our respects to their Elders past and present.</p>
<p class="abs copy">@2024 Copyrights <span class="pink">Tall Pine</span> All Rights Reserved</p>

</body>
</html>
```